Pet store web design

I would like to redesign my current online store (http://brindlecove.example)
I'm looking for a clean, modern design. Any ideas are welcome..

Industry/Entity Type

Pet

Number of Pages Required

3 page

```html
<!DOCTYPE html>
<html lang="en">
<head>
<meta charset="utf-8">
<title>Brindle Cove – Pet Store</title>
<link href="https://fonts.googleapis.com/css2?family=Open+Sans:wght@400;600;700;800&family=Oswald:wght@500;700&display=swap" rel="stylesheet">
<style>
:root{
  --yellow:#f6c500;
  --yellow-dark:#e0b000;
  --ink:#2b2b2b;
  --ink-soft:#555;
  --muted:#888;
  --page:#ececec;
  --white:#fff;
  --teal:#1ba4a6;
  --teal-dark:#137c7e;
  --red:#d6261d;
  --green:#76b82a;
  --footer:#2c2c2c;
  --footer-deep:#1f1f1f;
  --line:#dcdcdc;
}
*{box-sizing:border-box;margin:0;padding:0}
html,body{width:1200px;height:2184px;overflow:hidden}
body{background:var(--page);font-family:"Open Sans",Arial,sans-serif;color:var(--ink);font-size:12px;position:relative}
.wrap{position:absolute;left:80px;width:1040px}
.img{background:linear-gradient(135deg,#b9c58a,#6f8a4a)}

/* header */
.site-header{position:absolute;top:0;left:0;width:1200px;height:88px;background:var(--yellow)}
.logo{position:absolute;left:80px;top:18px;display:flex;align-items:center;gap:10px;font-family:"Oswald",sans-serif;font-weight:700;font-size:26px;color:var(--ink)}
.logo span.mark{width:30px;height:30px;border-radius:50%;background:var(--ink)}
.main-nav{position:absolute;left:440px;top:30px;display:flex}
.main-nav a{font-weight:700;font-size:12px;color:var(--ink);text-decoration:none;padding:8px 14px;border-left:1px solid rgba(255,255,255,.6)}
.main-nav a.active{background:var(--ink);color:var(--yellow)}
.utility{position:absolute;right:72px;top:6px;width:150px;height:22px;background:var(--white);border-radius:2px;font-size:10px;color:var(--muted);padding:4px 8px}
.cart{position:absolute;right:80px;top:36px;width:34px;height:34px;border-radius:50%;background:var(--ink);display:flex;align-items:center;justify-content:center}

/* hero */
.hero{position:absolute;top:88px;left:0;width:1200px;height:472px;background:linear-gradient(160deg,#9fb86a 0%,#c9d48e 45%,#7f9a55 100%)}
.hero-copy{position:absolute;right:90px;top:318px;text-align:right;color:var(--white)}
.hero-copy h2{font-family:"Oswald",sans-serif;font-size:38px;letter-spacing:1px}
.hero-copy p{font-size:14px;margin-top:4px}
.hero-copy .btn{display:inline-block;margin-top:10px;background:var(--yellow);color:var(--ink);font-weight:700;padding:7px 16px;font-size:12px}
.hero-dots{position:absolute;bottom:18px;left:560px;display:flex;gap:8px}
.hero-dots i{width:10px;height:10px;border-radius:50%;background:rgba(255,255,255,.6)}
.hero-dots i:first-child{background:var(--yellow)}

/* mega menu */
.mega{position:absolute;top:88px;left:260px;width:880px;height:300px;background:var(--white);box-shadow:0 4px 10px rgba(0,0,0,.2);padding:22px 24px}
.mega-cols{display:flex;gap:20px}
.mega-col{width:128px}
.mega-col a{display:block;font-size:11px;color:var(--ink-soft);padding:5px 0;border-bottom:1px solid #f0f0f0;text-decoration:none}
.mega-feature{position:absolute;right:24px;top:22px;width:240px;height:180px;background:linear-gradient(135deg,#d9c7a6,#8d7a5c)}

/* promo tiles */
.promos{top:580px;display:flex;gap:10px}
.promo{width:200px;height:220px;background:var(--white)}
.promo-head{height:52px;background:var(--red);color:var(--white);text-align:center;padding-top:8px}
.promo-head.green{background:var(--green)}
.promo-head b{display:block;font-size:15px}
.promo-head small{font-size:10px}
.promo .img{height:168px}

/* products */
.catalog{top:840px;height:360px;background:var(--white);padding:16px 20px}
.tabs{display:flex;border-bottom:2px solid var(--yellow)}
.tabs a{font-size:11px;font-weight:700;padding:6px 16px;color:var(--ink-soft);text-decoration:none}
.tabs a.active{background:var(--yellow);color:var(--ink)}
.grid{display:flex;gap:20px;margin-top:18px}
.card{width:184px}
.card .img{height:150px;background:linear-gradient(135deg,#e8e8e8,#bdbdbd)}
.card h4{font-size:10px;font-weight:600;margin-top:10px;color:var(--ink-soft)}
.card .meta{display:flex;justify-content:space-between;align-items:center;margin-top:6px}
.stars{color:var(--yellow-dark);font-size:11px;letter-spacing:1px}
.price{font-weight:700;color:var(--red);font-size:12px}
.add{display:block;margin-top:8px;width:100px;background:var(--yellow);font-size:10px;font-weight:700;text-align:center;padding:6px 0}

/* banner */
.banner{top:1220px;height:140px;background:var(--teal);text-align:center;color:var(--white);padding-top:26px;padding-left:120px}
.banner h2{font-family:"Oswald",sans-serif;font-size:38px;letter-spacing:2px}
.banner p{display:inline-block;background:var(--teal-dark);margin-top:6px;padding:5px 22px;font-family:"Oswald",sans-serif;font-size:17px;letter-spacing:1px}
.banner-pets{position:absolute;left:200px;top:1200px;width:140px;height:84px;background:linear-gradient(135deg,#d8b88a,#8b6a45);border-radius:4px}

/* most popular */
.popular{top:1448px;height:272px;display:flex;gap:20px}
.popular-intro{width:300px;background:var(--yellow);padding:28px 26px}
.popular-intro h3{font-family:"Oswald",sans-serif;font-size:38px;line-height:1;color:var(--ink)}
.popular-intro p{font-size:11px;line-height:1.6;margin-top:14px;color:var(--ink)}
.popular-list{flex:1;background:var(--white);display:flex;align-items:center;justify-content:space-around;position:relative;padding:0 40px}
.arrow{position:absolute;top:110px;width:24px;height:40px;display:flex;align-items:center;justify-content:center}
.arrow.l{left:8px}.arrow.r{right:8px}
.pop-card{width:180px;text-align:center}
.pop-card .img{height:140px;background:linear-gradient(135deg,#e6e6e6,#b5b5b5)}
.pop-card h4{font-size:10px;font-weight:600;margin-top:10px;color:var(--ink-soft)}
.pop-card .price{display:block;margin-top:6px;font-size:15px}

/* features */
.features{top:1744px;height:76px;display:flex;justify-content:space-between;align-items:center;padding:0 40px}
.feature{display:flex;align-items:center;gap:10px}
.feature .ico{width:42px;height:42px;border-radius:50%;background:var(--yellow);display:flex;align-items:center;justify-content:center}
.feature b{display:block;font-size:12px}
.feature small{font-size:10px;color:var(--muted)}

/* newsletter */
.newsletter{position:absolute;top:1840px;left:0;width:1200px;height:48px;background:#3a3a3a;color:var(--white)}
.newsletter .inner{position:absolute;left:80px;top:12px;width:1040px;display:flex;align-items:center;gap:16px}
.newsletter span{font-size:11px;width:440px}
.newsletter .field{width:380px;height:24px;background:var(--white);font-size:10px;color:var(--muted);padding:5px 8px}
.newsletter .sub{background:var(--yellow);color:var(--ink);font-weight:700;font-size:11px;padding:5px 26px}

/* footer */
.site-footer{position:absolute;top:1888px;left:0;width:1200px;height:272px;background:var(--footer);color:#cfcfcf}
.footer-cols{position:absolute;left:80px;top:26px;width:1040px;display:flex;gap:30px}
.footer-col{width:237px}
.footer-col h5{color:var(--white);font-size:13px;margin-bottom:12px}
.footer-col a,.footer-col li{display:block;font-size:11px;color:#bdbdbd;text-decoration:none;line-height:1.9;list-style:none}
.footer-col p{font-size:11px;line-height:1.7}
.f-logo{font-family:"Oswald",sans-serif;font-weight:700;font-size:20px;color:var(--white);display:flex;align-items:center;gap:8px;margin-bottom:10px}
.f-logo i{width:18px;height:18px;background:var(--yellow)}
.pay{display:flex;gap:6px;margin-top:10px}
.pay i{width:34px;height:22px;background:#4a4a4a;border-radius:2px}
.social{display:flex;gap:6px;margin-top:10px}
.social i{width:22px;height:22px;border-radius:50%;background:#555}
.footer-bottom{position:absolute;top:2160px;left:0;width:1200px;height:24px;background:var(--footer-deep);color:#999;font-size:10px;text-align:center;line-height:24px}
</style>
</head>
<body>

<header class="site-header">
  <div class="logo"><span class="mark"></span>Brindle Cove</div>
  <nav class="main-nav">
    <a href="#">DOGS</a><a href="#">CAT +</a><a href="#">FISH +</a><a href="#">SMALL PET +</a><a href="#">ABOUT US</a><a class="active" href="#">CONTACT US</a>
  </nav>
  <div class="utility">Search products…</div>
  <div class="cart"><svg width="18" height="18" viewBox="0 0 24 24"><path d="M3 4h3l2 11h11l2-8H7" fill="none" stroke="#f6c500" stroke-width="2"/><circle cx="10" cy="19" r="1.6" fill="#f6c500"/><circle cx="17" cy="19" r="1.6" fill="#f6c500"/></svg></div>
</header>

<section class="hero" role="img" aria-label="Photo of a dog being groomed outdoors on a lawn">
  <div class="hero-copy">
    <h2>GROOMING PRODUCTS</h2>
    <p>A selection of dog grooming products</p>
    <span class="btn">SHOP NOW</span>
  </div>
  <div class="hero-dots"><i></i><i></i><i></i></div>
</section>

<div class="mega">
  <div class="mega-cols">
    <div class="mega-col"><a>Dog Beds</a><a>Dog Carriers</a><a>Dog Clothing</a><a>Dog Bowls</a><a>Pet Seat Extension</a><a>Dog Crates</a><a>Dog Gates</a><a>Pet Water Dispenser</a><a>Dog Treadmills</a><a>Dog Training Collars</a></div>
    <div class="mega-col"><a>Dog Training Collars</a><a>Heated Mats</a><a>Dog Clothing</a><a>Dog Grooming</a><a>Dog Flaps</a><a>Pet Harness</a><a>Pet Blankets</a><a>Pet Fountains</a><a>Dog Lights</a><a>Dog Car Seats</a></div>
    <div class="mega-col"><a>Dog Toys</a><a>Soft Dog Collars</a><a>Dog Mattress</a><a>Dog Houses</a><a>Outdoor Clothing</a><a>Dog Whistle</a><a>Dog Leads</a><a>Dog Crate Covers</a><a>Pet Strollers</a><a>Dog Ramps</a></div>
    <div class="mega-col"><a>Pet Stairs</a><a>Dog Chew Beds</a><a>Chicken Houses</a><a>Dog Toilet Mats</a><a>Dog Cooling Mats</a><a>Rescue Lifts</a><a>Reflective Leashes</a><a>Pond Covers</a><a>Repeller Devices</a><a>Travel Bowls</a></div>
  </div>
  <div class="mega-feature" role="img" aria-label="Photo of a dog with a chew toy"></div>
</div>

<section class="wrap promos">
  <div class="promo"><div class="promo-head"><b>Fish / Winter</b><small>Security for your pets</small></div><div class="img" role="img" aria-label="Photo of a dog in a safety vest"></div></div>
  <div class="promo"><div class="promo-head"><b>Fish / Winter</b><small>Warm coats for colder days</small></div><div class="img" role="img" aria-label="Photo of a small dog in a winter coat"></div></div>
  <div class="promo"><div class="promo-head"><b>Fish / Winter</b><small>Keep them cosy all season</small></div><div class="img" role="img" aria-label="Photo of a red pet product"></div></div>
  <div class="promo"><div class="promo-head green"><b>Soft Rubber Toys</b><small>Safe toys for play time</small></div><div class="img" role="img" aria-label="Photo of rubber pet toys"></div></div>
  <div class="promo"><div class="promo-head"><b>Pet Dogs Bed</b><small>Soft beds for every size</small></div><div class="img" role="img" aria-label="Photo of a dog lying on a bed"></div></div>
</section>

<section class="wrap catalog">
  <nav class="tabs"><a class="active">NEW</a><a>CAT</a><a>FISH</a><a>BIRD</a><a>SMALL PET</a></nav>
  <div class="grid">
    <div class="card"><div class="img" role="img" aria-label="Product photo of a pet feeder"></div><h4>AUTOMATIC PET FEEDER BOWL</h4><div class="meta"><span class="stars">★★★★★</span><span class="price">£39.95</span></div><span class="add">ADD TO CART</span></div>
    <div class="card"><div class="img" role="img" aria-label="Product photo of a wooden dog kennel"></div><h4>WOODEN DOG KENNEL LARGE</h4><div class="meta"><span class="stars">★★★★☆</span><span class="price">£89.00</span></div><span class="add">ADD TO CART</span></div>
    <div class="card"><div class="img" role="img" aria-label="Product photo of a pet carrier"></div><h4>FOLDING PET CARRIER BAG</h4><div class="meta"><span class="stars">★★★★★</span><span class="price">£27.75</span></div><span class="add">ADD TO CART</span></div>
    <div class="card"><div class="img" role="img" aria-label="Product photo of a dog treadmill"></div><h4>DOG TREADMILL SMALL</h4><div class="meta"><span class="stars">★★★★☆</span><span class="price">£499.00</span></div><span class="add">ADD TO CART</span></div>
    <div class="card"><div class="img" role="img" aria-label="Product photo of a dog treadmill"></div><h4>DOG TREADMILL MEDIUM</h4><div class="meta"><span class="stars">★★★★★</span><span class="price">£549.00</span></div><span class="add">ADD TO CART</span></div>
  </div>
</section>

<section class="wrap banner">
  <h2>30 NEW PET PRODUCTS EVERY MONTH</h2>
  <p>FREE DELIVERY ON ORDERS OVER £70</p>
</section>
<div class="banner-pets" role="img" aria-label="Photo of two small dogs"></div>

<section class="wrap popular">
  <div class="popular-intro">
    <h3>MOST<br>POPULAR</h3>
    <p>The pet products our customers love most this season, picked from hundreds of reviews and ready to ship today.</p>
  </div>
  <div class="popular-list">
    <span class="arrow l"><svg width="14" height="24" viewBox="0 0 14 24"><path d="M12 2 2 12l10 10" fill="none" stroke="#888" stroke-width="2"/></svg></span>
    <div class="pop-card"><div class="img" role="img" aria-label="Product photo of a pet carrier"></div><h4>PET CARRIER – LARGE</h4><span class="price">£30.69</span></div>
    <div class="pop-card"><div class="img" role="img" aria-label="Product photo of a round dog bed"></div><h4>ROUND PLUSH DOG BED</h4><span class="price">£200.33</span></div>
    <div class="pop-card"><div class="img" role="img" aria-label="Product photo of a dog treadmill"></div><h4>DOG TREADMILL PRO</h4><span class="price">£603.80</span></div>
    <span class="arrow r"><svg width="14" height="24" viewBox="0 0 14 24"><path d="m2 2 10 10L2 22" fill="none" stroke="#888" stroke-width="2"/></svg></span>
  </div>
</section>

<section class="wrap features">
  <div class="feature"><span class="ico"><svg width="22" height="22" viewBox="0 0 24 24"><path d="M2 6h12v10H2zM14 10h4l3 3v3h-7z" fill="#2b2b2b"/><circle cx="6" cy="18" r="2" fill="#2b2b2b"/><circle cx="17" cy="18" r="2" fill="#2b2b2b"/></svg></span><div><b>Delivery Information</b><small>Free over £70</small></div></div>
  <div class="feature"><span class="ico"><svg width="22" height="22" viewBox="0 0 24 24"><path d="M4 12a8 8 0 1 0 3-6" fill="none" stroke="#2b2b2b" stroke-width="2.4"/><path d="M3 3v6h6" fill="none" stroke="#2b2b2b" stroke-width="2.4"/></svg></span><div><b>Returns Policy</b><small>30 day returns</small></div></div>
  <div class="feature"><span class="ico"><svg width="22" height="22" viewBox="0 0 24 24"><path d="M8 9a4 4 0 1 1 5 4c-1 .4-1 1-1 2.5" fill="none" stroke="#2b2b2b" stroke-width="2.4"/><circle cx="12" cy="19.5" r="1.5" fill="#2b2b2b"/></svg></span><div><b>Questions Ask</b><small>We are here to help</small></div></div>
  <div class="feature"><span class="ico"><svg width="22" height="22" viewBox="0 0 24 24"><path d="M6 3h4l1 5-2.5 1.5a11 11 0 0 0 6 6L16 13l5 1v4a2 2 0 0 1-2 2A16 16 0 0 1 4 5a2 2 0 0 1 2-2z" fill="#2b2b2b"/></svg></span><div><b>Call us Today Contact</b><small>Mon – Fri 9am – 5pm</small></div></div>
</section>

<section class="newsletter">
  <div class="inner">
    <span>Keep up to date with the latest from our pet store. Sign up now:</span>
    <span class="field">Enter your email address</span>
    <span class="sub">SUBSCRIBE</span>
  </div>
</section>

<footer class="site-footer">
  <div class="footer-cols">
    <div class="footer-col">
      <h5>ABOUT US</h5>
      <div class="f-logo"><i></i>Brindle Cove</div>
      <p>Welcome to Brindle Cove, your one stop shop for pet supplies. We bring quality products to you and your pets at fair prices every day.</p>
    </div>
    <div class="footer-col">
      <h5>SERVICES</h5>
      <ul><li>Pet Grooming</li><li>Pet Training</li><li>Gift Vouchers</li><li>Pet Insurance</li><li>Puppy Advice</li></ul>
      <h5 style="margin-top:14px">SHOP NOW</h5>
      <ul><li>Dogs</li><li>Cats</li><li>Fish</li></ul>
    </div>
    <div class="footer-col">
      <h5>SHOPPING ONLINE</h5>
      <ul><li>Delivery Information</li><li>Privacy Policy</li><li>Returns Policy</li><li>Terms and Conditions</li><li>FAQs</li></ul>
      <h5 style="margin-top:14px">WE ACCEPT</h5>
      <div class="pay"><i></i><i></i><i></i><i></i></div>
    </div>
    <div class="footer-col">
      <h5>CONTACT</h5>
      <ul><li>12 Harbour Lane, Kestwick</li><li>+44 0161 555 0148</li><li>hello@brindlecove.example</li><li>brindlecove.example</li></ul>
      <h5 style="margin-top:14px">LET'S KEEP IN TOUCH</h5>
      <div class="social"><i></i><i></i><i></i><i></i><i></i><i></i></div>
    </div>
  </div>
</footer>
<div class="footer-bottom">© 2014 Brindle Cove Store. All Rights Reserved</div>

</body>
</html>
```